Brindel Clear Springs needs a new business card design (we produce and sell pure bottled water)

We need a clean modern design for our new business cards, We have an existing logo which ultimately cannot be changed, however it could be slighty improved and the colours adjusted. We have this existing logo on all of our bottles, vehicles etc.

Our company slogan is "Clear at the source, fresh in every sip".
Along with our relevant company information
(Address, phone, website email etc) we will only be using names and not putting position titles for flexibilty.

We are looking for a clean, minimalist modern design.

You can view our website (if need of an update also!) to see our business.

Industry/Entity Type

Business

Contact Information for Business Card

Staff Name : XXXXXX XXXXXX
Address : 8/41 Tallowood St
Marwick Flats QLD 4172
Staff Mobile Number : 04XX XXX XXX
Office Phone Number : 07 3918 4520
Staff Email Address : XXXX@brindelclearsprings.com.au
Website : www.brindelclearsprings.com.au

Font styles to use
Sans Serif

Colors
cee9f5
33a6d7
0492cd
0455a3
3276b5
85abd2
cedeed

Requirements
Must have
• The ability to edit and change the staff members details as we will need to edit for each respective staff member (7 in total)

```html
<!DOCTYPE html>
<html lang="en">
<head>
<meta charset="utf-8">
<title>Brindel Clear Springs – Business Card</title>
<link rel="stylesheet" href="https://fonts.googleapis.com/css2?family=Open+Sans:wght@400;600;700;800&display=swap">
<style>
  :root {
    --backdrop: #ebebeb;
    --navy: #363687;
    --sky: #35a5d7;
    --paper: #ffffff;
    --ink: #111111;
    --ink-soft: #555555;
    --name-tint: #d8ddf3;
    --bottle-light: #f6f9fe;
    --bottle-mid: #e9f0fc;
  }
  * { margin: 0; padding: 0; box-sizing: border-box; }
  html, body {
    width: 1200px; height: 1200px; overflow: hidden;
    background: var(--backdrop);
    font-family: "Open Sans", Arial, sans-serif;
  }
  .canvas { position: relative; width: 1200px; height: 1200px; }
  .card {
    position: absolute; width: 760px; height: 434px;
    background: var(--paper); overflow: hidden;
  }
  .card--front { left: 238px; top: 138px; }
  .card--back  { left: 240px; top: 626px; }
  .card-shapes { position: absolute; inset: 0; width: 760px; height: 434px; }
  .text { position: absolute; white-space: nowrap; }

  /* front */
  .staff-name { left: 18px; top: 180px; color: var(--name-tint); font-size: 27px; letter-spacing: 2.5px; line-height: 36px; }
  .staff-name__first { font-weight: 700; display: block; }
  .staff-name__last { font-weight: 400; display: block; }
  .contact-phone { left: 447px; top: 120px; font-size: 15px; letter-spacing: 1px; line-height: 23px; color: var(--ink); }
  .contact-phone__office { color: var(--ink-soft); font-size: 14px; display: block; }
  .contact-address { left: 391px; top: 204px; font-size: 14px; letter-spacing: 0.8px; line-height: 19px; color: var(--ink); }
  .contact-email { left: 330px; top: 302px; font-size: 14px; letter-spacing: 0.8px; color: var(--ink); }

  /* back */
  .website { right: 24px; top: 52px; font-size: 14.5px; letter-spacing: 1px; color: var(--ink); }
  .slogan { left: 34px; top: 190px; font-size: 25px; letter-spacing: 1.5px; line-height: 35px; color: var(--paper); font-weight: 400; }
  .slogan span { display: block; }
  .brand { right: 22px; bottom: 22px; text-align: right; color: var(--navy); font-weight: 800; }
  .brand__mark { width: 40px; height: 40px; border-radius: 50%; background: var(--navy); margin: 0 0 10px auto; }
  .brand__name { font-size: 31px; line-height: 30px; letter-spacing: 0.5px; display: block; }
  .brand__sub { font-size: 15.5px; line-height: 20px; letter-spacing: 0.6px; display: block; }
</style>
</head>
<body>
<main class="canvas">

  <section class="card card--front" aria-label="Business card front">
    <svg class="card-shapes" viewBox="0 0 950 543" preserveAspectRatio="none">
      <defs>
        <linearGradient id="bottleFill" x1="0" y1="0" x2="1" y2="1">
          <stop offset="0" stop-color="var(--bottle-mid)"/>
          <stop offset="1" stop-color="var(--bottle-light)"/>
        </linearGradient>
      </defs>
      <rect class="bottle-photo" x="670" y="86" width="218" height="387" rx="40" fill="url(#bottleFill)" role="img" aria-label="Faint photo of a large bottled water jug"/>
      <polygon class="panel-navy" points="0,0 535,0 185,543 0,543" fill="var(--navy)"/>
      <polygon class="stripe-top" points="552,0 642,0 582,98 492,98" fill="var(--navy)"/>
      <polygon class="stripe-bottom" points="257,453 349,453 292,543 202,543" fill="var(--navy)"/>
      <g class="connectors" fill="var(--navy)">
        <polygon points="522,98 532,98 517,123 507,123"/>
        <polygon points="455,208 465,208 450,233 440,233"/>
        <polygon points="385,318 395,318 380,343 370,343"/>
        <polygon points="317,428 327,428 312,453 302,453"/>
      </g>
      <g class="tile-shadows" fill="var(--navy)">
        <polygon points="420,208 507,208 503,214 424,218"/>
        <polygon points="347,318 437,318 433,324 351,328"/>
        <polygon points="277,428 365,428 361,434 281,438"/>
      </g>
      <polygon class="tile tile--phone" points="462,123 562,123 507,208 420,208" fill="var(--sky)"/>
      <polygon class="tile tile--pin" points="420,233 492,233 437,318 347,318" fill="var(--sky)"/>
      <polygon class="tile tile--email" points="347,343 420,343 365,428 277,428" fill="var(--sky)"/>
      <g class="icon-phone" fill="var(--paper)">
        <path d="M466,157 q21,-12 42,0 l0,6 l-10,2 l0,-5 q-11,-4 -22,0 l0,5 l-10,-2 z"/>
        <path d="M474,164 l26,0 l6,20 l-38,0 z"/>
        <g fill="var(--sky)">
          <circle cx="481" cy="171" r="1.5"/><circle cx="487" cy="171" r="1.5"/><circle cx="493" cy="171" r="1.5"/>
          <circle cx="481" cy="176" r="1.5"/><circle cx="487" cy="176" r="1.5"/><circle cx="493" cy="176" r="1.5"/>
          <circle cx="487" cy="181" r="1.5"/>
        </g>
      </g>
      <path class="icon-pin" d="M419,298 C404,280 400,272 400,265 a19,19 0 0 1 38,0 c0,7 -4,15 -19,33 z M419,257 a8,8 0 1 0 0.1,0 z" fill="var(--paper)" fill-rule="evenodd"/>
      <text class="icon-at" x="345" y="400" font-family="Open Sans, Arial, sans-serif" font-size="44" fill="var(--paper)" text-anchor="middle">@</text>
    </svg>

    <h1 class="text staff-name">
      <span class="staff-name__first">ROWAN</span>
      <span class="staff-name__last">TILLEY</span>
    </h1>
    <p class="text contact-phone">Personal: 98 4127 6630<span class="contact-phone__office">Office: (07) 39184520</span></p>
    <p class="text contact-address">8/41 Tallowood St<br>Marwick Flats QLD 4172</p>
    <p class="text contact-email">rowan@brindelclearsprings.com.au</p>
  </section>

  <section class="card card--back" aria-label="Business card back">
    <svg class="card-shapes" viewBox="0 0 950 543" preserveAspectRatio="none" aria-hidden="true">
      <polygon class="panel-navy" points="0,0 536,0 186,543 0,543" fill="var(--navy)"/>
      <polygon class="stripe-sky" points="552,0 642,0 292,543 202,543" fill="var(--sky)"/>
      <rect class="slogan-bar" x="20" y="188" width="12" height="191" fill="var(--paper)"/>
    </svg>

    <p class="text website">www.brindelclearsprings.com.au</p>
    <p class="text slogan"><span>Clear at the source,</span><span>fresh in every sip</span></p>
    <div class="text brand">
      <div class="brand__mark"></div>
      <span class="brand__name">BRINDEL</span>
      <span class="brand__sub">CLEAR SPRINGS</span>
    </div>
  </section>

</main>
</body>
</html>
```